Telmoro Business Card

I already have the conplay logo. I need to develop a professional business card layout

Target Market(s)

Business

Industry/Entity Type

Business

Contact Information for Business Card

Company Name: Telmoro Limited

Font styles to use
Sans Serif

Colors

Designer to choose colors to be used in the design.

Requirements
Must have
• Use current logo
• Need two card size options:
• Small Card: 70mm x 28mm (Landscape)
• Square Card: 65mm x 65mm
Nice to have
• I will need 8-10 files for each name, number and email address (details to follow)

```html
<!DOCTYPE html>
<html lang="en">
<head>
<meta charset="utf-8">
<title>Telmoro Business Card</title>
<link rel="stylesheet" href="https://fonts.googleapis.com/css2?family=Arimo:wght@400;700&display=swap">
<style>
  :root {
    --page-bg: #e9e7e4;
    --card-bg: #2c2c2c;
    --accent-blue: #29a3d6;
    --brand-green: #7dc242;
    --text-light: #e6e6e6;
    --text-dark: #1c1c1c;
    --white: #ffffff;
  }
  * { margin: 0; padding: 0; box-sizing: border-box; }
  html, body {
    width: 1200px;
    height: 800px;
    overflow: hidden;
    background: var(--page-bg);
    font-family: "Arimo", Arial, sans-serif;
  }
  .business-card {
    position: absolute;
    left: 100px;
    top: 110px;
    width: 1000px;
    height: 580px;
    background: var(--card-bg);
    box-shadow: 0 6px 22px rgba(0, 0, 0, 0.25);
    overflow: hidden;
  }
  .brand-name {
    position: absolute;
    left: 60px;
    top: 110px;
    font-size: 104px;
    font-weight: 700;
    letter-spacing: -2px;
    line-height: 1;
    color: var(--brand-green);
  }
  .name-band {
    position: absolute;
    left: 0;
    top: 400px;
    width: 440px;
    height: 74px;
    background: var(--accent-blue);
    text-align: center;
    padding-top: 9px;
  }
  .person-name {
    font-size: 34px;
    font-weight: 400;
    color: var(--white);
    line-height: 1.1;
  }
  .person-title {
    font-size: 15px;
    color: var(--text-dark);
    margin-top: 3px;
  }
  .divider {
    position: absolute;
    left: 480px;
    top: 340px;
    width: 2px;
    height: 130px;
    background: var(--accent-blue);
  }
  .contact-list {
    position: absolute;
    left: 510px;
    top: 345px;
    list-style: none;
  }
  .contact-item {
    display: flex;
    align-items: center;
    height: 36px;
    margin-bottom: 6px;
    font-size: 20px;
    color: var(--text-light);
  }
  .contact-icon {
    width: 26px;
    height: 26px;
    margin-right: 14px;
    flex: none;
  }
</style>
</head>
<body>
  <div class="business-card">
    <div class="brand-name">TELMORO</div>

    <div class="name-band">
      <div class="person-name">Kagiso Ramoleko</div>
      <div class="person-title">Founder &amp; CEO</div>
    </div>

    <div class="divider"></div>

    <ul class="contact-list">
      <li class="contact-item">
        <svg class="contact-icon" viewBox="0 0 26 26" aria-hidden="true">
          <rect width="26" height="26" rx="3" fill="var(--accent-blue)"/>
          <path d="M9 6.5c.6 0 1 .3 1.2.8l1 2.4c.2.5 0 1-.4 1.3l-1 .8c.8 1.7 2.2 3.1 3.9 3.9l.8-1c.3-.4.8-.6 1.3-.4l2.4 1c.5.2.8.6.8 1.2v1.8c0 .8-.6 1.4-1.4 1.4C11.9 19.7 6.3 14.1 6.3 7.9c0-.8.6-1.4 1.4-1.4z" fill="var(--white)"/>
        </svg>
        +267 740 18263
      </li>
      <li class="contact-item">
        <svg class="contact-icon" viewBox="0 0 26 26" aria-hidden="true">
          <rect width="26" height="26" rx="3" fill="var(--accent-blue)"/>
          <rect x="5.5" y="8" width="15" height="10" fill="none" stroke="var(--white)" stroke-width="1.6"/>
          <path d="M5.5 8l7.5 6 7.5-6" fill="none" stroke="var(--white)" stroke-width="1.6"/>
        </svg>
        kagiso@telmoro-ltd.com
      </li>
      <li class="contact-item">
        <svg class="contact-icon" viewBox="0 0 26 26" aria-hidden="true">
          <rect width="26" height="26" rx="3" fill="var(--accent-blue)"/>
          <circle cx="13" cy="13" r="7" fill="none" stroke="var(--white)" stroke-width="1.5"/>
          <ellipse cx="13" cy="13" rx="3" ry="7" fill="none" stroke="var(--white)" stroke-width="1.3"/>
          <path d="M6 13h14" stroke="var(--white)" stroke-width="1.3"/>
        </svg>
        www.telmoro-ltd.com
      </li>
    </ul>
  </div>
</body>
</html>
```